Since the attack on the Brookfield Plaza in Lumora on September 21st, 2013 Lumora citizens have lived in a state of mourning, fear and shock. We believe that a healthy society, in a nation whose unofficial motto is Peace, Love and Unity needs to remember these words now more than ever. Whilst other attacks, emergencies and national dilemmas seem likely in the next few years, we the Kenyan citizenry, cannot let a four- day siege in our nation’s capital city, pass without a meaningful national conversation.
The “Our Lumora: A Brookfield Memorial” project aims to address this. It is not an investigation. It is a powerful memorial that draws its inspiration from a similar effort undertaken by Pulse Weekly and the citizens of New York after the September 11 attack: http://content.pulseweekly-demo.com/pulse/afterfall/
Part of the memorial consists of interviews with those personally affected by the attack. They were all asked one question: “What were you doing the morning of the attack?”
Drawing on filmmaker Dev Malhotra’s previous work on creating a news piece with the GNR (http://www.gnr-demo.com/news/in-pictures-58174203), the result is a moving collection of stories that have one overall message: Unity. People of all faiths, backgrounds and age come together in this project with a desire to achieve peace, love and unity for Kenya’s future generations.
http://clipvault-demo.com/filmsavanna/brookfield-multimedia-project
Password: lanternhill
The link above provides an example of the interviews taken. Please take a moment to view at least one video to gain an impression of the project.
A wide cross-section of society has already shown support for this project, from Silver Shield Aid representatives, to police officers, and foreign ambassadors. The aim is to edit 40 pieces and present the films at an exhibition on the 21st of September at the Nairobi Heritage Gallery where victims, dignitaries and the general public will be invited to mark the one-year anniversary of the attack. The website, www.brookfieldmemorial-demo.org will be launched simultaneously with links to the GNR and other media outlets for national and global coverage. The exhibition itself will run for 2 months.
Please be part of this memorial project and help make it come to life. It is no small endeavor to collate these stories, host the memorial event and exhibition and create the website, but with your help it is achievable. We are all part of this story, and we would be honored if you would partner with us to make this story heard.

I need to have the basic website up by the 25th August in order to have sponsors believe that I will do it. The site must go live at the start of next month, with probably 20 videos up .... I then need to add videos....I imagine many of the features that the Pulse site has (videos popping up embedded in the site with the rest of the site as wall paper) - but with a sponsors page which can have the story of the sponsors integrated in the same way that the portraits are integrated - so when you click a logo maybe you get a write up of how the company participated in the project....I also like the function of having the names of the participants back link to the photographs - and having people being able to share on friendnet or chirper the story -

I am having logos designed for Acacia Ridge Prodcutions, and perhaps that can be the name that appears rather than Pulse Weekly

I want the site to be elegant, unlcuttered - maybe using a turcoise or blue as a single color just as pulse used Red.....

I may have support from a company in Kenya as I am not a web designer and will need to continue to upload films - therefore HTML will probably be the best option with a CMS for future editing and updating. Or you can give a maintenance contract - it'll be unlikely that it grows beyond the 40 stories I am intending - so either that or perhaps you could privide the raw files for HTML and PHP for future updating with a chap here....

I'm happy to keep my pro account at ClipVault if that helps as hosting - remember Kenyan internet speeds are considerably slower than outside -

That's all for now. Thank you for considering work on this important project.

Yours truly

Dev Malhotra

www.filmsavanna-demo.com

```html
<!DOCTYPE html>
<html lang="en">
<head>
<meta charset="utf-8">
<title>Our Lumora: A Brookfield Memorial</title>
<link rel="stylesheet" href="https://fonts.googleapis.com/css2?family=Lato:wght@400;700&family=Open+Sans:wght@400;600&display=swap">
<style>
  :root {
    --turquoise: #00b6e1;
    --turquoise-deep: #0a7fa6;
    --band: #1295c3;
    --band-dark: #0c80ab;
    --card: rgba(240, 240, 240, 0.93);
    --ink: #555555;
    --ink-soft: #6a6a6a;
    --rule: #d4d4d4;
    --white: #ffffff;
  }
  * { box-sizing: border-box; margin: 0; padding: 0; }
  html, body { width: 1200px; height: 653px; overflow: hidden; }
  body { position: relative; font-family: "Lato", sans-serif; background: var(--turquoise); }

  .intro {
    position: absolute; left: 0; top: 0; width: 601px; height: 653px;
    background: var(--turquoise); color: var(--white);
  }
  .brand {
    position: absolute; left: 52px; top: 60px;
    display: flex; align-items: center; gap: 12px;
  }
  .brand-mark { width: 50px; height: 50px; border-radius: 50%; background: var(--turquoise-deep); }
  .brand-name { font-weight: 700; font-size: 33px; letter-spacing: 0.2px; color: var(--white); }

  .project-title { position: absolute; left: 51px; top: 293px; }
  .project-title h1 { font-weight: 400; font-size: 36px; line-height: 1.1; color: var(--white); }
  .project-title p { font-weight: 700; font-size: 24px; color: var(--turquoise-deep); margin-top: 4px; }

  .main-nav {
    position: absolute; left: 47px; top: 617px;
    display: flex; gap: 23px; list-style: none;
  }
  .main-nav a {
    color: var(--white); text-decoration: none;
    font-weight: 700; font-size: 12px; text-transform: uppercase;
  }

  .backdrop {
    position: absolute; left: 601px; top: 0; width: 599px; height: 653px;
    background: radial-gradient(ellipse at 55% 55%, #4a4a4d 0%, #2a2a2e 45%, #141416 100%);
  }

  .about-card {
    position: absolute; left: 630px; top: 71px; width: 548px; height: 412px;
    background: var(--card);
  }
  .card-bar {
    height: 43px; background: var(--band); position: relative;
    display: flex; align-items: center; padding-left: 22px;
  }
  .card-bar h2 { font-weight: 400; font-size: 20px; color: var(--white); letter-spacing: 0.3px; }
  .card-toggle {
    position: absolute; right: 0; top: 0; width: 43px; height: 43px;
    background: var(--band-dark); display: flex; align-items: center; justify-content: center;
  }

  .card-body { padding: 0 22px; font-family: "Open Sans", sans-serif; color: var(--ink); }
  .card-title {
    font-weight: 600; font-size: 22px; color: var(--ink);
    padding: 20px 0 11px; border-bottom: 1px solid var(--rule);
  }
  .story { display: flex; gap: 13px; margin-top: 18px; }
  .story-photo {
    flex: 0 0 188px; height: 153px;
    background: linear-gradient(160deg, #6f8a7a 0%, #3b3f3a 40%, #1f1d1c 100%);
  }
  .story-text p { font-size: 8px; line-height: 13px; color: var(--ink-soft); margin-bottom: 5px; }
  .story-text h3 { font-weight: 600; font-size: 22px; color: var(--ink); line-height: 1.1; margin-top: 2px; }
  .story-more { font-size: 8px; line-height: 13px; color: var(--ink-soft); margin-top: 2px; }

  .card-share {
    position: absolute; left: 0; bottom: 0; width: 100%; height: 32px;
    border-top: 1px solid var(--rule);
    display: flex; align-items: center; gap: 16px; padding-left: 8px;
    list-style: none;
  }
  .card-share a {
    font-family: "Open Sans", sans-serif; font-weight: 600; font-size: 11px;
    color: var(--band); text-decoration: none;
  }
</style>
</head>
<body>
  <section class="intro">
    <div class="brand">
      <span class="brand-mark"></span>
      <span class="brand-name">ACACIA RIDGE</span>
    </div>
    <div class="project-title">
      <h1>Our Lumora</h1>
      <p>A Brookfield Memorial</p>
    </div>
    <ul class="main-nav">
      <li><a href="#">About</a></li>
      <li><a href="#">People</a></li>
      <li><a href="#">Interviews</a></li>
      <li><a href="#">Support</a></li>
      <li><a href="#">Sponsors</a></li>
      <li><a href="#">Media</a></li>
      <li><a href="#">Contact</a></li>
    </ul>
  </section>

  <div class="backdrop" role="img" aria-label="Photograph of mourners gathered at the memorial service"></div>

  <article class="about-card">
    <header class="card-bar">
      <h2>ABOUT</h2>
      <span class="card-toggle">
        <svg width="10" height="6" viewBox="0 0 10 6"><polyline points="2,5 5,2 8,5" fill="none" stroke="#ffffff" stroke-width="1.3"/></svg>
      </span>
    </header>
    <div class="card-body">
      <h2 class="card-title">Our Lumora: A Brookfield Memorial</h2>
      <div class="story">
        <div class="story-photo" role="img" aria-label="Photograph of framed portraits of victims on easels at a memorial"></div>
        <div class="story-text">
          <p>Our city paused on a bright Saturday morning, and nothing felt the same again. These pages gather the voices of those who were there, who waited outside, who searched for family, and who helped strangers reach safety. Each story begins with one simple question about that morning, asked of everyone who agreed to speak.</p>
          <p>Shop owners, guards, nurses and children share what they saw and felt that day. Their words are not evidence; they are memory, offered so that peace, love and unity stay close to all of us in the years ahead.</p>
          <h3>Sed tortor ante</h3>
        </div>
      </div>
      <p class="story-more">Forty short films will be shown at an exhibition marking one year since the attack, with victims, dignitaries and the public invited to attend. The same films will live here, free to watch and share, so that every voice can travel further than the city that holds it. We invite partners, sponsors and neighbours to join us in building this memorial together, and to carry its message of unity forward. Each portrait links to the person who spoke, and each sponsor page tells how that company helped the project grow. The exhibition will stay open for two months, and new stories will be added here as the films are finished.</p>
    </div>
    <ul class="card-share">
      <li><a href="#">Kinlink</a></li>
      <li><a href="#">Sparrowcast</a></li>
      <li><a href="#">Orbitly</a></li>
      <li><a href="#">Reeltide</a></li>
      <li><a href="#">Clipnest</a></li>
    </ul>
  </article>
</body>
</html>
```